Ansprechendes Layout für Geschichte von Oldtimern
Grossartiges Design, supernette Zusammenarbeit, megaschnelle Rückmeldung auf meine dusseligen Fragen - dass "Kastrel Ubo" sich meines Projektes angenommen hat, war ein echter Glückstreffer! Ich bin sowohl mit dem Ergebnis als auch mit der Kommunikation während des gesamten Prozesses absolut happy! Das hat richtig Spaß gemacht und auf meine Oldtimer-"Broschüre" bin ich stolz wie Bolle... Schade, dass man hier nicht 10 Sterne vergeben kann - "Kastrel Ubo" hätte sie verdient!
Zielgruppe
Ich mache mich aktuell selbstständig als Solo-Freiberuflerin (Redakteurin) mit dem Projekt 'Die Lack-Ballade': Ich schreibe für Oldtimer-Besitzer die Lebensgeschichte ihres Oldtimers auf - lebendig und augenzwinkernd. Zielgruppe: Oldtimer-Besitzer, die die Historie ihres Wagens als individuelles 'Buch' haben möchten; für sich selbst oder auch als Verkaufsargument beim Weiterverkauf des Oldtimers.
Aufgabenstellung
Mein Text wird auf hochwertigem Papier (einseitig) gedruckt , im Format A4 quer. Ein paar gut platzierte Fotos sollen den Text 'auflockern'. Für dieses Layout von Titelseite sowie Text & Fotos suche ein 'hinreißendes' Design (Schriften und Layout). Die fertigen Seiten werden dann in einer Druckerei ausgedruckt und in einen A4 Querformat-Klemmbinder 'reingesteckt'. Deswegen muss links entsprechend viel Rand/Platz gelassen werden. Wichtig ist mir eine sehr edle und hochwertige Anmutung des Layouts. Es soll kein 'Bildband' werden, die Fotos ergänzen lediglich den Text, der 'im Mittelpunkt' steht.

```html
<!DOCTYPE html>
<html lang="de">
<head>
<meta charset="utf-8">
<title>Die Lack-Ballade – Seitenlayout</title>
<link rel="stylesheet" href="https://fonts.googleapis.com/css2?family=Carlito:wght@400&family=Fira+Sans:wght@400;500&display=swap">
<style>
  :root {
    --gold: #b8a25b;
    --charcoal: #3a3a3a;
    --band: #333333;
    --ink: #1a1a1a;
    --paper: #ffffff;
    --bg: #ffffff;
    --photo-navy: #2a3246;
    --photo-green: #5f7a45;
  }
  * { margin: 0; padding: 0; box-sizing: border-box; }
  html, body { width: 1200px; height: 2554px; overflow: hidden; background: var(--bg); }
  .canvas { position: relative; width: 1200px; height: 2554px; }

  .page {
    position: absolute;
    left: 88px;
    width: 1036px;
    height: 732px;
    background: var(--paper);
    box-shadow: 3px 2px 4px rgba(0,0,0,0.28);
  }
  .page--one { top: 152px; }
  .page--two { top: 924px; }
  .page--three { top: 1688px; }

  .page__rule-top { position: absolute; left: 0; top: 0; width: 100%; height: 6px; background: var(--charcoal); }
  .page__rule-gold { position: absolute; left: 0; top: 684px; width: 100%; height: 6px; background: var(--gold); }
  .page__band { position: absolute; left: 0; top: 698px; width: 100%; height: 34px; background: var(--band); }

  .brand {
    position: absolute;
    right: 70px;
    top: 58px;
    display: flex;
    align-items: center;
    gap: 10px;
  }
  .brand__mark { width: 18px; height: 18px; background: var(--gold); }
  .brand__name {
    font-family: "Fira Sans", sans-serif;
    font-weight: 500;
    font-size: 33px;
    color: var(--gold);
    letter-spacing: 0.5px;
    white-space: nowrap;
  }
  .brand__tagline {
    position: absolute;
    right: 80px;
    top: 148px;
    font-family: "Fira Sans", sans-serif;
    font-weight: 400;
    font-size: 13.5px;
    letter-spacing: 0.4px;
    color: var(--gold);
    white-space: nowrap;
  }

  .photo { position: absolute; left: 173px; width: 353px; }
  .photo--wedding { top: 228px; height: 345px; background: linear-gradient(180deg, var(--photo-green) 0%, var(--photo-navy) 35%, var(--photo-navy) 75%, var(--photo-green) 100%); }
  .photo--profile { top: 302px; height: 199px; background: linear-gradient(135deg, #6d8a55 0%, var(--photo-navy) 40%, #1f2535 80%, #cfcfc8 100%); }

  .story {
    position: absolute;
    font-family: "Carlito", sans-serif;
    font-size: 13.6px;
    line-height: 18.45px;
    color: var(--ink);
    text-align: justify;
    hyphens: auto;
  }
  .story--beside-photo { left: 565px; width: 369px; top: 224px; }
  .story--col-left { left: 173px; width: 365px; top: 299px; }
  .story--col-right { left: 574px; width: 365px; top: 299px; }
  .story--beside-small { left: 565px; width: 369px; top: 298px; }
</style>
</head>
<body>
<main class="canvas">

  <section class="page page--one">
    <div class="page__rule-top"></div>
    <div class="brand"><span class="brand__mark"></span><span class="brand__name">Die Lack-Ballade</span></div>
    <p class="brand__tagline">DIE GESCHICHTE DEINES OLDTIMERS</p>
    <div class="photo photo--wedding" role="img" aria-label="Foto: dunkelblaue Oldtimer-Limousine mit Blumenschmuck auf der Motorhaube, auf einer Wiese geparkt"></div>
    <p class="story story--beside-photo">Kein Wunder also, dass unsere gemeinsame Ostseeküsten-Tour vor ein paar Jahren ein voller Erfolg wurde: eine wunderschöne, ganz entspannte Reise! Herrlich! „Da, wo wir angehalten haben, war immer sofort eine Menschentraube und hat den tollen Oldtimer bestaunt…“, hat der Torvald seiner Bekannten erzählt. Und ich hab’ aus seinen Worten ganz genau den Stolz auf mich herausgehört. Und natürlich hat er ihr auch gleich die wunderschönen Fotos von der Hochzeit seines Gesellen Jannik neulich gezeigt. Da hatte ich nämlich zum ersten Mal die große Ehre, das Hochzeitsauto sein zu dürfen. Mit einem zauberhaften Blumenschmuck auf der Motorhaube! Ich sah wirklich hinreißend aus und musste aufpassen, dass ich der wunderschönen Braut nicht die Show stehle… Ich glaube übrigens, dass der Jannik mich auch richtig gerne mag. Jedenfalls hat er abends, als die ganze Aufregung vorbei war und ich bei Jannik übernachten durfte, dem Torvald noch eine Nachricht aufs Handy geschickt: „Dein Baby ist im Bett“, hat er geschrieben. Und dazu ein Foto mitgeschickt von mir in seiner Garage. Der Mann weiß, was sich gehört.</p>
    <div class="page__rule-gold"></div>
    <div class="page__band"></div>
  </section>

  <section class="page page--two">
    <div class="page__rule-top"></div>
    <div class="brand"><span class="brand__mark"></span><span class="brand__name">Die Lack-Ballade</span></div>
    <p class="brand__tagline">DIE GESCHICHTE DEINES OLDTIMERS</p>
    <p class="story story--col-left">Was man im Übrigen ja nicht von allen Verkehrsteilnehmern heutzutage behaupten kann…: Vor kurzem haben der Torvald und ich eine entspannte Sonntagsfahrt aufs Land hinaus gemacht – und plötzlich zischt doch irgend so ein neumodischer Verwandter meiner weitverzweigten Sippschaft an uns vorbei und überholt uns mit einem irren Tempo. Gemeinhin bringt mich so ein Verhalten von angeberischen Jungspunden wie dem nicht aus der Fassung. Aber dieses Mal ausnahmsweise doch - denn der Kerl war fast lautlos! Ich habe mich beinahe zu Tode erschreckt, weil von dem rein gar nichts zu hören war! Wie macht der das?!</p>
    <p class="story story--col-right">Hat der denn keinen anständig röhrenden Motor unter der Haube? Keine ratternden Kolben? Torvald hat irgendetwas Unverständliches von „E-Mobilität“ oder so ähnlich gemurmelt – keine Ahnung, was das für ein neumodischer Kram sein soll. Aber Autos, die fast unhörbar rasend schnell fahren, sind mir irgendwie suspekt. Ob deren Besitzer sie wohl genauso lieben wie der Torvald mich liebt? Kann man ein geräuschloses Auto überhaupt lieben? Na, ich weiß ja nicht so recht… Jedenfalls bin ich immer für meinen herrlichen Motorsound gelobt worden, der in den Ohren von echten Oldtimerfans wie wunderbare Musik klingt.</p>
    <div class="page__rule-gold"></div>
    <div class="page__band"></div>
  </section>

  <section class="page page--three">
    <div class="page__rule-top"></div>
    <div class="brand"><span class="brand__mark"></span><span class="brand__name">Die Lack-Ballade</span></div>
    <p class="brand__tagline">DIE GESCHICHTE DEINES OLDTIMERS</p>
    <div class="photo photo--profile" role="img" aria-label="Foto: Seitenansicht der dunkelblauen Oldtimer-Limousine mit Weißwandreifen"></div>
    <p class="story story--beside-small">Neulich stand mal wieder die Hauptuntersuchung an. Nach so vielen Jahren sehe ich diesem Geschehen meist mit entspannter Lässigkeit entgegen – ich weiß, dass ich trotz meiner inzwischen 54 Jahre nach wie vor ein echter Hingucker bin. Die einzige Aufregung bestand dieses Mal darin, dass mir der Torvald vorher noch schicke Weißwandreifen spendiert hat, die mir ganz wunderbar stehen! Ich muss ihn doch mal fragen, ob sein allererstes Auto, eine himmelblaue Brenner Kugel, die er sich damals mit seinem Bruder geteilt hat, eigentlich auch solche Weißwandreifen hatte? Aber das mit der Kugel ist dann schon wieder eine ganz andere Geschichte…</p>
    <div class="page__rule-gold"></div>
    <div class="page__band"></div>
  </section>

</main>
</body>
</html>
```